Aviation Maintenance & Aircraft Cleaning Website

We need a fairly simple modern sleek website . Our company does aviation maintenance , aircraft cleaning , maintenance tracking . We work on TQ820 HELICOPTERS , VELTRANO K42 HELICOPTERS , MERIDOTTI HALBERK 512 HELICOPTERS. We would like a website that can be mobile as well with future ideas that an app where you could book cleanings and maintenance . Right now the biggest thing is for our customer to see a website , be able to book our services online and see our staff . the website must be modern and clean .

Target Market(s)

Aviation maintenance , aviation cleaning ,

Logo Text

KM but 1 image unlike the one i uploaded which is two . Im open for different aviation designs

Number of Pages Required

5+ page

Font styles to use
Serif

Requirements
Must have
• Home page , Aircraft Maintenance , Aircraft Cleaning , About Us , Contact , Careers

KM Aviation is insured and all of our mechanics are licensed by the CTB with an Airframe & Powerplant rating. ( FRONT PAGE )

Home page should have a simple nice picture of a TQ820 or Veltrano K42 . My Logo as you can see seems like two logos . i would like 1 logo and made of the two if possible . (New ideas are welcome . )

Book a Cleaning Calendar should in the aircraft cleaning page . The aircraft cleaning page should have a picture of cleaning a helicopter or private jet .

Aircraft maintenance page should have a mechanic working on a helicopter . The Page should have a fast way to contact us .

We are a mobile AOG team who is available 24/7 . What we do
Scheduled & Unscheduled aircraft maintenance
Major & Minor repairs
STC installations
Aircraft Weight & Balance
Aircraft Painting
Aircraft Cleaning
Maintenance Tracking Utilizing Tracking Programs or spreadsheets
Removal & Installation of Components
Aircraft Pre Buy Inspections
Nice to have
• modern , sleek , aviation

Meet the Staff

Picture with Headset on flying in a helicopter

CEO Tobias Whitcombe

Tobias Has been an aircraft mechanic for over 10 years . He has worked for the largest sightseeing & charter tourism company in the New York City area as well as repair stations & manufacturers. He has aircraft specific training to the Corvane TQ820 & Tovrin 4K7. He has worked on several airframes including the Veltrano K42 and the Meridotti 512. He has held every position in an aircraft maintenance department from mechanic up to Director of Maintenance . His work ethic and ability to manage mechanics in a organized and structured way gives any department or inspection a clear direction .

About Us

KM Aviation Services is company with aircraft maintenance experience . We focus on inspections of aircraft . Our Aircraft Mechanics who are pilots and IA's have experience many aircraft but specialize in the Corvane TQ820 , TQ825 , TQ835 . The Veltrano K42 and Meridotti Halberk 512 . Our focus is safety and to maintain aircraft day in and day out so our customer can operate the aircraft safely while keeping up with all the manufacturers inspections .

We know aircraft maintenance & maintenance planning . Leave the technical and tedious things to us . Get in your aircraft and fly knowing you have the best maintenance crew in the business.

```html
<!DOCTYPE html>
<html lang="en">
<head>
<meta charset="utf-8">
<title>KM Aviation – Website Pages</title>
<link rel="stylesheet" href="https://fonts.googleapis.com/css2?family=Playfair+Display:wght@400;700&family=Montserrat:wght@400;500;600;700&display=swap">
<style>
:root{
  --board:#e6e6e6;
  --navy:#0e1630;
  --navy-2:#1f2f66;
  --blue:#1c3ea3;
  --blue-soft:#2b4aa8;
  --ink:#1b1b1b;
  --grey:#8a8d96;
  --line:#d5d7dd;
  --faint:#e9edf6;
  --pending:#f5c21a;
  --booked:#ee2323;
  --white:#ffffff;
}
*{box-sizing:border-box;margin:0;padding:0}
html,body{width:1200px;height:2971px;overflow:hidden;background:var(--board)}
body{position:relative;font-family:"Montserrat",sans-serif;color:var(--ink)}
.board-label{position:absolute;font:400 17px "Montserrat",sans-serif;color:#3a3a3a;letter-spacing:.3px}
.page{position:absolute;background:var(--white);overflow:hidden;box-shadow:0 6px 18px rgba(0,0,0,.14)}
.col-left{left:56px;width:504px}
.col-right{left:647px;width:503px}
.abs{position:absolute}
.serif{font-family:"Playfair Display",serif}

/* header */
.site-header{position:absolute;top:0;left:0;right:0;height:28px;background:var(--white);z-index:2}
.brand{position:absolute;left:52px;top:7px;font:700 9px "Playfair Display",serif;color:var(--blue);line-height:1}
.brand small{display:block;font-size:5px;letter-spacing:1px;margin-top:1px}
.main-nav{position:absolute;right:53px;top:0;height:28px;display:flex;align-items:center;gap:22px;font-size:6.3px;color:#555}
.main-nav .active{color:var(--blue);border-bottom:1px solid var(--blue);padding-bottom:1px}
.main-nav .btn-contact{background:var(--blue);color:var(--white);padding:3px 8px}

/* footer */
.site-footer{position:absolute;left:0;right:0;bottom:0;height:112px;background:var(--navy);color:var(--white)}
.footer-brand{position:absolute;left:52px;top:16px;font:700 12px "Playfair Display",serif;line-height:1}
.footer-brand small{display:block;font-size:6px;letter-spacing:1.5px;margin-top:2px}
.footer-contact{position:absolute;left:52px;top:46px;font-size:5.3px;line-height:14px}
.footer-contact div{display:flex;align-items:center;gap:4px}
.footer-contact svg{width:6px;height:6px;fill:var(--white)}
.footer-dots{position:absolute;left:54px;top:86px;display:flex;gap:13px}
.footer-dots span{width:5px;height:5px;border-radius:50%;background:var(--white)}
.footer-col{position:absolute;top:33px;font-size:5.5px;line-height:18px;color:#c9ccd6}
.footer-col h4{font-size:5.8px;font-weight:600;color:var(--white)}
.footer-copy{position:absolute;right:8px;bottom:10px;font-size:4px;color:#b8bbc6}
.notch{position:absolute;top:-12px;left:425px;width:0;height:0;border-left:12px solid transparent;border-right:12px solid transparent;border-bottom:12px solid var(--navy)}

/* shared pieces */
.photo{position:absolute}
.btn{position:absolute;background:var(--blue);color:var(--white);font-size:5px;display:flex;align-items:center;justify-content:center}
.section-title{position:absolute;left:52px;right:52px;display:flex;align-items:center;gap:10px;font:700 17px "Playfair Display",serif;color:var(--navy);white-space:nowrap;line-height:22px}
.section-title::before,.section-title::after{content:"";flex:1;height:1px;background:var(--navy)}
.field{position:absolute;background:var(--white);font-size:4px;color:#999;padding:2px 4px;border:1px solid #e2e2e2}
.crumb{position:absolute;right:52px;font-size:3.6px;color:#555}
.faint-mark{position:absolute;font:700 150px "Playfair Display",serif;color:var(--faint);line-height:1;letter-spacing:-6px}

/* home */
.hero-copy{position:absolute;color:var(--white)}
.hero-copy h1{font:700 17px/21px "Playfair Display",serif}
.hero-copy p{font-size:4.2px;margin-top:6px}
.about-title{font:700 17px/20px "Playfair Display",serif;color:var(--navy);text-align:right}
.body-copy{font-size:4.6px;line-height:7.4px;color:#555}
.services-box{position:absolute;left:127px;top:697px;width:249px;height:166px;background:var(--navy-2);padding:13px 14px;color:var(--white)}
.services-box h3{font:700 11.5px "Playfair Display",serif;margin-bottom:6px}
.services-box li{list-style:none;display:flex;align-items:center;gap:5px;font-size:5.5px;height:14.7px}
.services-box svg{width:6px;height:6px}
.service-tile{position:absolute;top:1030px;width:163px;height:162px;display:flex;align-items:center;justify-content:center;font:400 11px "Playfair Display",serif;color:var(--white);letter-spacing:.6px}

/* calendar */
.calendar{position:absolute;left:52px;top:352px;width:200px;height:176px;border:1px solid #cfd2d9;background:var(--white)}
.cal-month{position:absolute;left:8px;top:10px;font-size:5.5px;font-weight:600;color:var(--blue)}
.cal-arrows{position:absolute;right:10px;top:6px;display:flex;gap:6px}
.cal-arrows span{width:11px;height:11px;border:1px solid #999;border-radius:50%;display:flex;align-items:center;justify-content:center;font-size:6px;color:#333}
.cal-grid{position:absolute;left:6px;top:27px;width:190px;display:grid;grid-template-columns:repeat(7,1fr);row-gap:7px;font-size:5px;text-align:center;color:#333}
.cal-grid span{height:12px;line-height:12px;width:12px;margin:0 auto}
.cal-grid .head{color:#888}
.cal-grid .muted{color:#c2c2c2}
.cal-grid .pending{background:var(--pending)}
.cal-grid .booked{background:var(--booked);color:var(--white)}
.cal-legend{position:absolute;left:10px;top:156px;display:flex;gap:14px;font-size:4px;color:#666}
.cal-legend span{display:flex;align-items:center;gap:3px}
.cal-legend i{display:inline-block;width:8px;height:8px}
.booking-panel{position:absolute;left:252px;top:352px;width:198px;height:176px;background:var(--navy);color:var(--white)}

/* career */
.perk{position:absolute;width:120px}
.perk h4{font-size:7.4px;font-weight:600;color:var(--blue)}
.perk p{font-size:4px;line-height:5.5px;color:#888;margin-top:3px}
.job-tabs{position:absolute;top:822px;left:0;right:0;font:400 8px "Playfair Display",serif;color:#777}
.job-tabs span{position:absolute}
.job-tabs .active{color:var(--blue);font-weight:700;border-bottom:1px solid var(--blue)}
.job-row{position:absolute;left:52px;width:365px;height:46px;border-bottom:1px solid #aaa}
.job-row h4{font-size:6.3px;font-weight:600;margin-top:4px}
.job-row p{font-size:3.8px;color:#999;margin-top:3px}
.job-row .btn{right:0;top:11px;width:54px;height:15px;font-size:5.5px}
</style>
</head>
<body>

<div class="board-label" style="left:56px;top:42px">Home Page</div>
<div class="board-label" style="left:647px;top:196px">Maintenance Page</div>
<div class="board-label" style="left:647px;top:724px">Cleaning Page</div>
<div class="board-label" style="left:647px;top:1580px">About Us Page</div>
<div class="board-label" style="left:56px;top:1633px">Career Page</div>
<div class="board-label" style="left:647px;top:2423px">Contact Us Page</div>

<svg width="0" height="0" style="position:absolute">
  <defs>
    <symbol id="i-phone" viewBox="0 0 24 24"><path d="M6.6 10.8a15 15 0 0 0 6.6 6.6l2.2-2.2a1 1 0 0 1 1-.25 11.4 11.4 0 0 0 3.6.6 1 1 0 0 1 1 1V20a1 1 0 0 1-1 1A17 17 0 0 1 3 4a1 1 0 0 1 1-1h3.5a1 1 0 0 1 1 1c0 1.250.2 2.45.6 3.6a1 1 0 0 1-.25 1z"/></symbol>
    <symbol id="i-mail" viewBox="0 0 24 24"><path d="M2 5h20v14H2zm2 2v.5l8 5 8-5V7l-8 5z"/></symbol>
    <symbol id="i-clock" viewBox="0 0 24 24"><circle cx="12" cy="12" r="10"/><path d="M12 6v6l4 2" stroke="#0e1630" stroke-width="2" fill="none"/></symbol>
    <symbol id="i-tick" viewBox="0 0 24 24"><circle cx="12" cy="12" r="11" fill="#fff"/><path d="M7 12.5l3.2 3.2L17 9" stroke="#1f2f66" stroke-width="2.6" fill="none"/></symbol>
  </defs>
</svg>

<!-- ================= HOME ================= -->
<section class="page col-left" style="top:92px;height:1460px">
  <header class="site-header">
    <div class="brand">KM<small>AVIATION</small></div>
    <nav class="main-nav"><span class="active">Home</span><span>About Us</span><span>Maintenance</span><span>Cleaning</span><span>Careers</span><span class="btn-contact">Contact Us</span></nav>
  </header>
  <div class="abs" style="left:0;top:28px;width:187px;height:170px;background:var(--navy)"></div>
  <div class="hero-copy" style="left:53px;top:74px">
    <h1>Your Safety,<br>Our Priority</h1>
    <p>Let us take care of your aircraft</p>
  </div>
  <div class="btn" style="left:53px;top:140px;width:58px;height:13px">Contact Us</div>
  <div class="photo" role="img" aria-label="White helicopter on the apron at dusk" style="left:187px;top:28px;width:317px;height:170px;background:linear-gradient(180deg,#3a5a9a 0%,#6f86b8 45%,#9aa3b4 62%,#3d4150 100%)"></div>

  <div class="faint-mark" style="left:12px;top:232px">KM</div>
  <div class="abs about-title" style="left:110px;top:274px;width:57px">About<br>Us</div>
  <p class="abs body-copy" style="left:190px;top:268px;width:184px">KM Aviation Services is a company with aircraft maintenance experience. We focus on inspections of aircraft. Our Aircraft Mechanics who are pilots and IA's have experienced many aircraft but specialize in the Corvane TQ820, TQ825, TQ835. The Veltrano K42 and Meridotti Halberk 512. Our focus is safety and to maintain aircraft day in and day out so our customers can operate the aircraft safely while keeping up with all the manufacturer's inspections.</p>
  <div class="btn" style="left:190px;top:337px;width:42px;height:11px;font-size:4.5px">Learn More</div>

  <div class="photo" role="img" aria-label="Mechanic inspecting a helicopter engine in a hangar" style="left:0;top:413px;width:168px;height:168px;background:linear-gradient(160deg,#c9ccd2,#6d717a 60%,#3b3e45)"></div>
  <div class="photo" role="img" aria-label="Jet aircraft parked in a hangar, front view" style="left:168px;top:413px;width:168px;height:168px;background:linear-gradient(180deg,#2a2a30,#7a6a58 55%,#4a4440)"></div>
  <div class="photo" role="img" aria-label="Mechanic working on a helicopter turbine" style="left:336px;top:413px;width:168px;height:168px;background:linear-gradient(200deg,#b7bcc6,#5a5f6a 55%,#2c2f36)"></div>

  <div class="abs" style="left:0;top:581px;width:504px;height:341px;background:var(--navy)"></div>
  <h2 class="abs serif" style="left:0;width:504px;top:628px;text-align:center;font-weight:700;font-size:16px;line-height:22px;color:var(--white)">We are a mobile AOG team who is<br>available 24/7</h2>
  <div class="services-box">
    <h3>What we do:</h3>
    <ul>
      <li><svg><use href="#i-tick"/></svg>Scheduled &amp; Unscheduled aircraft maintenance</li>
      <li><svg><use href="#i-tick"/></svg>Major &amp; Minor repairs</li>
      <li><svg><use href="#i-tick"/></svg>Aircraft Weight &amp; Balance</li>
      <li><svg><use href="#i-tick"/></svg>Aircraft Painting</li>
      <li><svg><use href="#i-tick"/></svg>Aircraft Cleaning</li>
      <li><svg><use href="#i-tick"/></svg>Maintenance Tracking Utilizing Tracking Programs/Spreadsheets</li>
      <li><svg><use href="#i-tick"/></svg>Removal &amp; Installation of Components</li>
      <li><svg><use href="#i-tick"/></svg>Aircraft Pre Buy Inspections</li>
    </ul>
  </div>

  <div class="section-title" style="top:966px">Services</div>
  <p class="abs" style="left:0;width:504px;top:1007px;text-align:center;font-size:7.5px;color:#333">What do you need?</p>
  <div class="service-tile" role="img" aria-label="Mechanic hands working with tools, blue overlay" style="left:88px;background:linear-gradient(160deg,#4b5fa8,#2e3f86)">MAINTENANCE</div>
  <div class="service-tile" role="img" aria-label="Helicopter engine bay, blue overlay" style="left:257px;background:linear-gradient(200deg,#5066ad,#2b3b7e)">CLEANING</div>
  <p class="abs" style="left:0;width:504px;top:1210px;text-align:center;font-size:7.3px;line-height:15px;color:#333">KM Aviation is insured and all of our mechanics are licensed by the CTB with<br>an Airframe &amp; Powerplant rating. Click the menu above to learn more.</p>

  <footer class="site-footer">
    <span class="notch" style="border-bottom-color:var(--blue)"></span>
    <div class="footer-brand">KM<small>AVIATION</small></div>
    <div class="footer-contact"><div><svg><use href="#i-phone"/></svg>+555010142</div><div><svg><use href="#i-mail"/></svg>info@kmaviation.com</div></div>
    <div class="footer-dots"><span></span><span></span><span></span></div>
    <div class="footer-col" style="left:187px"><h4>About Us</h4><div>Meet Our Staff</div><div>Career</div></div>
    <div class="footer-col" style="left:277px"><h4>Contact Us</h4><div>FAQ</div><div>Blog</div></div>
    <div class="footer-col" style="left:349px"><h4>Support</h4><div>Services</div><div>Procedures</div></div>
    <div class="footer-copy">©2020 KM AVIATION</div>
  </footer>
</section>

<!-- ================= MAINTENANCE ================= -->
<section class="page col-right" style="top:247px;height:427px">
  <header class="site-header">
    <div class="brand">KM<small>AVIATION</small></div>
    <nav class="main-nav"><span>Home</span><span>About Us</span><span class="active">Maintenance</span><span>Cleaning</span><span>Careers</span><span class="btn-contact">Contact Us</span></nav>
  </header>
  <div class="photo" role="img" aria-label="Mechanic tightening a bolt on a helicopter rotor assembly" style="left:0;top:28px;width:254px;height:244px;background:linear-gradient(150deg,#c8cbd0,#7c8088 45%,#5c7a3e 75%,#a23022)"></div>
  <div class="abs" style="left:254px;top:28px;width:249px;height:244px;background:var(--navy)"></div>
  <div class="hero-copy" style="left:287px;top:68px">
    <h1 style="font-size:15.5px;line-height:19px">Take care of your<br>Aircraft with us</h1>
    <p style="font-size:5.3px;line-height:8px;width:150px;margin-top:5px">Please contact us in order to discuss your needs, so that we could provide the best solution possible.</p>
  </div>
  <div class="field" style="left:287px;top:145px;width:151px;height:13px">Full Name</div>
  <div class="field" style="left:287px;top:163px;width:151px;height:13px">Email</div>
  <div class="field" style="left:287px;top:181px;width:151px;height:13px">Subject</div>
  <div class="field" style="left:287px;top:199px;width:151px;height:28px">Your message here...</div>
  <div class="btn" style="left:390px;top:233px;width:48px;height:11px;font-size:4.5px">Send Message</div>
  <div class="abs" style="left:0;top:272px;width:503px;height:45px;background:var(--blue)"></div>
  <footer class="site-footer">
    <div class="footer-brand">KM<small>AVIATION</small></div>
    <div class="footer-contact"><div><svg><use href="#i-phone"/></svg>+555010142</div><div><svg><use href="#i-mail"/></svg>info@kmaviation.com</div></div>
    <div class="footer-dots"><span></span><span></span><span></span></div>
    <div class="footer-col" style="left:187px"><h4>About Us</h4><div>Meet Our Staff</div><div>Career</div></div>
    <div class="footer-col" style="left:277px"><h4>Contact Us</h4><div>FAQ</div><div>Blog</div></div>
    <div class="footer-col" style="left:349px"><h4>Support</h4><div>Services</div><div>Procedures</div></div>
    <div class="footer-copy">©2020 KM AVIATION</div>
  </footer>
</section>

<!-- ================= CLEANING ================= -->
<section class="page col-right" style="top:776px;height:720px">
  <header class="site-header">
    <div class="brand">KM<small>AVIATION</small></div>
    <nav class="main-nav"><span>Home</span><span>About Us</span><span>Maintenance</span><span class="active">Cleaning</span><span>Careers</span><span class="btn-contact">Contact Us</span></nav>
  </header>
  <div class="photo" role="img" aria-label="Open helicopter engine bay being serviced" style="left:0;top:28px;width:503px;height:244px;background:linear-gradient(120deg,#1c2c6a 0%,#4f5a72 35%,#9a8a6a 60%,#c9a872 80%,#6a5a40 100%)"></div>
  <div class="crumb" style="top:275px">Home &gt; Aircraft Cleaning Service</div>
  <div class="section-title" style="top:303px;font-size:15.5px">Book your aircraft cleaning with us</div>

  <div class="calendar">
    <div class="cal-month">Oktober 2020</div>
    <div class="cal-arrows"><span>‹</span><span>›</span></div>
    <div class="cal-grid">
      <span class="head">S</span><span class="head">M</span><span class="head">T</span><span class="head">W</span><span class="head">T</span><span class="head">F</span><span class="head">S</span>
      <span class="muted">27</span><span class="muted">28</span><span class="muted">29</span><span class="muted">30</span><span class="booked">1</span><span>2</span><span>3</span>
      <span>4</span><span>5</span><span class="pending">6</span><span class="pending">7</span><span class="pending">8</span><span class="pending">9</span><span>10</span>
      <span>11</span><span>12</span><span>13</span><span>14</span><span>15</span><span>16</span><span>17</span>
      <span>18</span><span class="pending">19</span><span>20</span><span>21</span><span class="booked">22</span><span class="booked">23</span><span>24</span>
      <span>25</span><span>26</span><span class="pending">27</span><span class="booked">28</span><span>29</span><span>30</span><span>31</span>
    </div>
    <div class="cal-legend">
      <span><i style="background:var(--pending)"></i>Pending</span>
      <span><i style="background:var(--booked)"></i>Booked</span>
      <span><i style="border:1px solid #999"></i>Available</span>
    </div>
  </div>
  <div class="booking-panel">
    <p class="abs" style="left:22px;top:20px;width:160px;font-size:7.3px;line-height:11px">Pick your booking date and fill your information below.</p>
    <div class="field" style="left:22px;top:62px;width:150px;height:12px">Full Name</div>
    <div class="field" style="left:22px;top:80px;width:150px;height:12px">Email</div>
    <div class="field" style="left:22px;top:98px;width:150px;height:12px">Phone Number</div>
    <div class="field" style="left:22px;top:116px;width:60px;height:12px;background:var(--navy-2);color:#aab;border-color:#445">Number of visitors ▾</div>
    <div class="btn" style="left:22px;top:145px;width:48px;height:16px;font-size:5.5px">Book Now</div>
  </div>

  <footer class="site-footer">
    <span class="notch" style="left:424px;border-bottom-color:var(--blue)"></span>
    <div class="footer-brand">KM<small>AVIATION</small></div>
    <div class="footer-contact"><div><svg><use href="#i-phone"/></svg>+555010142</div><div><svg><use href="#i-mail"/></svg>info@kmaviation.com</div></div>
    <div class="footer-dots"><span></span><span></span><span></span></div>
    <div class="footer-col" style="left:187px"><h4>About Us</h4><div>Meet Our Staff</div><div>Career</div></div>
    <div class="footer-col" style="left:277px"><h4>Contact Us</h4><div>FAQ</div><div>Blog</div></div>
    <div class="footer-col" style="left:349px"><h4>Support</h4><div>Services</div><div>Procedures</div></div>
    <div class="footer-copy">©2020 KM AVIATION</div>
  </footer>
</section>

<!-- ================= ABOUT ================= -->
<section class="page col-right" style="top:1624px;height:756px">
  <header class="site-header">
    <div class="brand">KM<small>AVIATION</small></div>
    <nav class="main-nav"><span>Home</span><span class="active">About Us</span><span>Maintenance</span><span>Cleaning</span><span>Careers</span><span class="btn-contact">Contact Us</span></nav>
  </header>
  <div class="abs" style="left:0;top:28px;width:503px;height:63px;background:var(--blue)"></div>
  <h2 class="abs serif" style="left:52px;top:63px;font-size:11px;font-weight:700;color:var(--white)">About Us</h2>
  <div class="crumb" style="top:84px;color:#dfe4f3">Home &gt; About Us</div>

  <div class="faint-mark" style="left:10px;top:112px">KM</div>
  <div class="abs about-title" style="left:100px;top:156px;width:68px;text-align:left">Who<br>We Are</div>
  <div class="abs body-copy" style="left:189px;top:144px;width:190px">
    <p>KM Aviation Services is a company with aircraft maintenance experience. We focus on inspections of aircraft. Our Aircraft Mechanics who are pilots and IA's have experienced many aircraft but specialize in the Corvane TQ820, TQ825, TQ835. The Veltrano K42 and Meridotti Halberk 512. Our focus is safety and to maintain aircraft day in and day out so our customers can operate the aircraft safely while keeping up with all the manufacturer's inspections.</p>
    <p style="margin-top:6px">We know aircraft maintenance &amp; maintenance planning. Leave the technical and tedious things to us. Get in your aircraft and fly knowing you have the best maintenance crew in the business.</p>
  </div>

  <div class="section-title" style="top:305px;left:120px;right:120px">Meet the Staff</div>
  <div class="abs" style="left:0;top:402px;width:503px;height:217px;background:var(--navy)"></div>
  <div class="photo" role="img" aria-label="Portrait of the CEO wearing a headset inside a helicopter" style="left:187px;top:337px;width:128px;height:128px;border-radius:50%;border:3px solid var(--white);background:linear-gradient(160deg,#cfd3d8,#7e858e 55%,#3b4048)"></div>
  <p class="abs" style="left:0;width:503px;top:476px;text-align:center;font-size:8px;font-weight:600;color:var(--white)">CEO Tobias Whitcombe</p>
  <p class="abs" style="left:104px;top:493px;width:294px;height:65px;background:var(--blue);color:#dfe4f3;font-size:4.4px;line-height:7.4px;padding:6px 14px;text-align:center">Tobias has been an aircraft mechanic for over 10 years. He has worked for the largest sightseeing &amp; charter tourism company in the New York City area as well as repair stations &amp; manufacturers. He has aircraft specific training to the Corvane TQ820 &amp; Tovrin 4K7. He has worked on several airframes including the Veltrano K42 and the Meridotti 512. He has held every position in an aircraft maintenance department from mechanic up to Director of Maintenance. His work ethic and ability to manage mechanics in an organized and structured way gives any department or inspection a clear direction.</p>
  <div class="abs" style="left:0;top:619px;width:503px;height:26px;background:var(--blue)"></div>

  <footer class="site-footer">
    <span class="notch" style="left:424px;border-bottom-color:var(--white)"></span>
    <div class="footer-brand">KM<small>AVIATION</small></div>
    <div class="footer-contact"><div><svg><use href="#i-phone"/></svg>+555010142</div><div><svg><use href="#i-mail"/></svg>info@kmaviation.com</div></div>
    <div class="footer-dots"><span></span><span></span><span></span></div>
    <div class="footer-col" style="left:187px"><h4>About Us</h4><div>Meet Our Staff</div><div>Career</div></div>
    <div class="footer-col" style="left:277px"><h4>Contact Us</h4><div>FAQ</div><div>Blog</div></div>
    <div class="footer-col" style="left:349px"><h4>Support</h4><div>Services</div><div>Procedures</div></div>
    <div class="footer-copy">©2020 KM AVIATION</div>
  </footer>
</section>

<!-- ================= CAREER ================= -->
<section class="page col-left" style="top:1673px;height:1219px">
  <header class="site-header">
    <div class="brand">KM<small>AVIATION</small></div>
    <nav class="main-nav"><span>Home</span><span>About Us</span><span>Maintenance</span><span>Cleaning</span><span class="active">Careers</span><span class="btn-contact">Contact Us</span></nav>
  </header>
  <div class="abs" style="left:0;top:28px;width:187px;height:170px;background:var(--navy)"></div>
  <div class="hero-copy" style="left:53px;top:88px"><h1>Let's Work<br>With Us</h1></div>
  <div class="btn" style="left:53px;top:135px;width:58px;height:13px">View Jobs</div>
  <div class="photo" role="img" aria-label="Two mechanics working beside a white helicopter" style="left:187px;top:28px;width:317px;height:170px;background:linear-gradient(150deg,#9aa0a8,#e6e8ec 40%,#6a6f78 70%,#2f3238)"></div>

  <div class="section-title" style="top:249px;left:88px;right:88px">About Working Here</div>
  <div class="perk" style="left:119px;top:316px"><h4>Conducive Environtment</h4><p>Enjoy challenging work and a satisfying job without any hierarchy</p></div>
  <div class="perk" style="left:289px;top:316px"><h4>Shared Success</h4><p>Equity ownership and opportunity await</p></div>
  <div class="perk" style="left:119px;top:381px"><h4>Healthy Meals and Snacks</h4><p>Food is in the house so it feels like home</p></div>
  <div class="perk" style="left:289px;top:381px"><h4>Medical Insurance</h4><p>We've got you covered, literally!</p></div>
  <div class="perk" style="left:119px;top:443px"><h4>Best Gadgets</h4><p>Pamper the tech savvy in you with gadgets and advanced technology</p></div>
  <div class="perk" style="left:289px;top:443px"><h4>Culture of Learning</h4><p>Regular brown bag lunches to keep the brain rejuvenated</p></div>

  <div class="photo" role="img" aria-label="Mechanic inspecting an engine" style="left:0;top:535px;width:168px;height:167px;background:linear-gradient(160deg,#b9bdc4,#6a6f78 55%,#2f3238)"></div>
  <div class="photo" role="img" aria-label="Crew next to a helicopter in a hangar" style="left:168px;top:535px;width:168px;height:167px;background:linear-gradient(180deg,#d8dade,#8e939b 55%,#4a4e55)"></div>
  <div class="photo" role="img" aria-label="Pilot with headset in the cockpit" style="left:336px;top:535px;width:168px;height:167px;background:linear-gradient(200deg,#9ea4ad,#4f545c 60%,#24272c)"></div>

  <div class="section-title" style="top:757px;left:94px;right:94px">Open Positions</div>
  <div class="job-tabs">
    <span class="active" style="left:52px">Technician</span>
    <span style="left:144px">Marketing</span>
    <span style="left:236px">Finance</span>
    <span style="left:318px">Other</span>
  </div>
  <div class="job-row" style="top:860px"><h4>Aircraft Technician</h4><p>San Francisco, Full Time</p><div class="btn">Apply Now</div></div>
  <div class="job-row" style="top:906px"><h4>Aircraft Technician</h4><p>New Delhi, Part Time</p><div class="btn">Apply Now</div></div>
  <div class="job-row" style="top:952px"><h4>Technical Trainer</h4><p>San Francisco, Full Time</p><div class="btn">Apply Now</div></div>
  <div class="job-row" style="top:998px"><h4>Technician Suppervisor</h4><p>San Francisco, Full Time</p><div class="btn">Apply Now</div></div>

  <footer class="site-footer">
    <span class="notch" style="border-bottom-color:var(--blue)"></span>
    <div class="footer-brand">KM<small>AVIATION</small></div>
    <div class="footer-contact"><div><svg><use href="#i-phone"/></svg>+555010142</div><div><svg><use href="#i-mail"/></svg>info@kmaviation.com</div></div>
    <div class="footer-dots"><span></span><span></span><span></span></div>
    <div class="footer-col" style="left:187px"><h4>About Us</h4><div>Meet Our Staff</div><div>Career</div></div>
    <div class="footer-col" style="left:277px"><h4>Contact Us</h4><div>FAQ</div><div>Blog</div></div>
    <div class="footer-col" style="left:349px"><h4>Support</h4><div>Services</div><div>Procedures</div></div>
    <div class="footer-copy">©2020 KM AVIATION</div>
  </footer>
</section>

<!-- ================= CONTACT ================= -->
<section class="page col-right" style="top:2468px;height:478px">
  <header class="site-header">
    <div class="brand">KM<small>AVIATION</small></div>
    <nav class="main-nav"><span>Home</span><span>About Us</span><span>Maintenance</span><span>Cleaning</span><span>Careers</span><span class="btn-contact">Contact Us</span></nav>
  </header>
  <div class="abs" style="left:0;top:28px;width:503px;height:63px;background:var(--blue)"></div>
  <h2 class="abs serif" style="left:52px;top:63px;font-size:11px;font-weight:700;color:var(--white)">Contact Us</h2>
  <div class="crumb" style="top:84px;color:#dfe4f3">Home &gt; Contact Us</div>

  <div class="abs" style="left:65px;top:120px;width:351px;height:177px;background:#ececec"></div>
  <div class="abs" style="left:416px;top:120px;width:22px;height:176px;background:var(--blue)"></div>
  <div class="abs" style="left:78px;top:137px;width:1px;height:24px;background:var(--navy)"></div>
  <h3 class="abs serif" style="left:86px;top:137px;font-size:10.5px;line-height:13px;font-weight:700;color:var(--navy)">Feel free to contact<br>us anytime</h3>
  <div class="field" style="left:86px;top:181px;width:149px;height:13px">Full Name</div>
  <div class="field" style="left:86px;top:198px;width:149px;height:13px">Email</div>
  <div class="field" style="left:86px;top:216px;width:149px;height:13px">Subject</div>
  <div class="field" style="left:86px;top:233px;width:149px;height:28px">Your message here...</div>
  <div class="btn" style="left:187px;top:267px;width:48px;height:12px;font-size:4.5px">Send Message</div>

  <div class="abs" style="left:265px;top:169px;width:150px;height:112px;background:var(--navy);color:var(--white);font-size:5.3px">
    <h3 class="serif" style="position:absolute;left:11px;top:16px;font-size:11px;font-weight:700">Info</h3>
    <div style="position:absolute;left:11px;top:47px;line-height:17px">
      <div style="display:flex;align-items:center;gap:4px"><svg width="6" height="6" fill="#fff"><use href="#i-phone"/></svg>+555010142</div>
      <div style="display:flex;align-items:center;gap:4px"><svg width="6" height="6" fill="#fff"><use href="#i-mail"/></svg>info@kmaviation.com</div>
      <div style="display:flex;align-items:center;gap:4px"><svg width="6" height="6" fill="#fff"><use href="#i-clock"/></svg>08.00 - 17.00</div>
    </div>
  </div>

  <footer class="site-footer">
    <span class="notch" style="left:424px;border-bottom-color:var(--blue)"></span>
    <div class="footer-brand">KM<small>AVIATION</small></div>
    <div class="footer-contact"><div><svg><use href="#i-phone"/></svg>+555010142</div><div><svg><use href="#i-mail"/></svg>info@kmaviation.com</div></div>
    <div class="footer-dots"><span></span><span></span><span></span></div>
    <div class="footer-col" style="left:187px"><h4>About Us</h4><div>Meet Our Staff</div><div>Career</div></div>
    <div class="footer-col" style="left:277px"><h4>Contact Us</h4><div>FAQ</div><div>Blog</div></div>
    <div class="footer-col" style="left:349px"><h4>Support</h4><div>Services</div><div>Procedures</div></div>
    <div class="footer-copy">©2020 KM AVIATION</div>
  </footer>
</section>

</body>
</html>
```